Veloria Pain Management (this is the name of our clinics)

We are a medical group who will open a few new offices to see patients who are interested in medical cannabis therapy. We want to express this in a poster or a life size stand-alone cardboard ad to inform patients that 'this is the place'. We may also want to use the electronic ad on an e-billboard. We will not dispense any of the cannabis on sit but we will see patients and issue prescriptions and user cards, and we will align those patients with a federal grower who will deliver the meds (cannabis oil) to their place. We dont have a logo yet, so we want that as well.
Updates

Target Market(s)

Patients with repetitive strain injuries and other chronic pains, or post traumatic stress disorder from the military of victims of traumatic accidents or assaults.

Industry/Entity Type

Medical And Science

Requirements
Must have
• A poster showing a patient in clinic setting with our clinic name (Veloria Pain Management)

```html
<!DOCTYPE html>
<html lang="en">
<head>
<meta charset="utf-8">
<title>Veloria Pain Management – Medical Cannabis Therapy</title>
<link href="https://fonts.googleapis.com/css2?family=Patrick+Hand&family=Merriweather:ital,wght@0,400;1,400&family=Open+Sans:wght@400;600&display=swap" rel="stylesheet">
<style>
  :root {
    --green: #6ea243;
    --green-dark: #4f8030;
    --green-light: #a9cf86;
    --white: #ffffff;
    --photo-wall: #b9b2a6;
    --photo-wood: #c69a5c;
    --photo-floor: #7d7a74;
  }
  html, body {
    margin: 0;
    padding: 0;
    overflow: hidden;
    background: #ffffff;
  }
  .poster {
    position: relative;
    width: 800px;
    height: 1200px;
    overflow: hidden;
    background: var(--green);
    font-family: "Open Sans", sans-serif;
    color: var(--white);
  }
  .clinic-photo {
    position: absolute;
    left: 0; top: 0;
    width: 800px; height: 690px;
    background:
      linear-gradient(90deg, rgba(90,120,70,0.35) 0%, rgba(0,0,0,0) 18%),
      linear-gradient(180deg, var(--photo-wood) 0%, #b89466 30%, var(--photo-wall) 31%, #a8a39a 70%, var(--photo-floor) 100%);
  }
  .waves {
    position: absolute;
    left: 0; top: 0;
    width: 800px; height: 1200px;
  }
  .header-brand {
    position: absolute;
    left: 420px; top: 22px;
    width: 366px; height: 66px;
    border: 2px solid rgba(255,255,255,0.7);
    box-sizing: border-box;
    text-align: center;
    font-family: "Merriweather", serif;
    color: var(--green-dark);
    background: rgba(255,255,255,0.25);
  }
  .header-brand .name {
    display: block;
    font-size: 26px;
    line-height: 36px;
    margin-top: 4px;
  }
  .header-brand .tagline {
    display: block;
    font-size: 13px;
    letter-spacing: 4px;
    text-transform: uppercase;
  }
  .call-badge {
    position: absolute;
    left: -30px; top: 650px;
    width: 250px; height: 250px;
    border-radius: 50%;
    background: var(--white);
    border: 12px solid var(--green-light);
    box-sizing: border-box;
    color: var(--green);
    text-align: center;
  }
  .call-badge .label {
    display: block;
    margin-top: 76px;
    margin-left: 30px;
    font-size: 34px;
    font-weight: 600;
  }
  .call-badge .phone {
    display: block;
    margin-left: 30px;
    font-size: 27px;
    font-weight: 600;
  }
  .therapy-title {
    position: absolute;
    left: 440px; top: 670px;
    margin: 0;
    font-family: "Patrick Hand", cursive;
    font-weight: 400;
    font-size: 66px;
    line-height: 78px;
    text-align: center;
    width: 300px;
    color: var(--white);
  }
  .contact-list {
    position: absolute;
    left: 26px; top: 962px;
    margin: 0; padding: 0;
    list-style: none;
    font-size: 19px;
  }
  .contact-list li {
    display: flex;
    align-items: center;
    gap: 12px;
    height: 34px;
  }
  .contact-list svg { width: 20px; height: 20px; }
  .service-note {
    position: absolute;
    left: 380px; top: 940px;
    width: 400px;
    margin: 0;
    font-size: 20px;
    line-height: 33px;
  }
  .footer-brand {
    position: absolute;
    left: 26px; top: 1110px;
    font-family: "Merriweather", serif;
    color: var(--white);
  }
  .footer-brand .name {
    display: block;
    font-size: 36px;
    line-height: 44px;
  }
  .footer-brand .tagline {
    display: block;
    font-size: 15px;
    letter-spacing: 5px;
    text-transform: uppercase;
  }
</style>
</head>
<body>
<main class="poster">
  <div class="clinic-photo" role="img" aria-label="Patient sitting on a bench in a clinic waiting area drinking from a cup, with a potted plant beside her"></div>

  <svg class="waves" viewBox="0 0 800 1200" aria-hidden="true">
    <path d="M0 700 C 240 640 560 600 800 500 L800 1200 L0 1200 Z" fill="var(--green)"/>
    <path d="M0 672 C 240 612 560 572 800 472" fill="none" stroke="var(--white)" stroke-width="34"/>
    <path d="M390 900 C 360 740 520 640 700 628" fill="none" stroke="var(--white)" stroke-width="7" stroke-linecap="round"/>
    <path d="M420 910 C 560 930 760 900 770 780 C 778 700 750 660 740 640" fill="none" stroke="var(--white)" stroke-width="7" stroke-linecap="round"/>
    <circle cx="718" cy="612" r="26" fill="var(--white)"/>
  </svg>

  <div class="header-brand">
    <span class="name">Veloria</span>
    <span class="tagline">Pain Management</span>
  </div>

  <div class="call-badge">
    <span class="label">CALL US</span>
    <span class="phone">555 014 2736</span>
  </div>

  <h1 class="therapy-title">Medical Cannabis Therapy.</h1>

  <ul class="contact-list">
    <li>
      <svg viewBox="0 0 20 20" aria-hidden="true"><circle cx="10" cy="10" r="8" fill="none" stroke="#fff" stroke-width="2"/><path d="M2 10h16M10 2c-4 4-4 12 0 16M10 2c4 4 4 12 0 16" fill="none" stroke="#fff" stroke-width="1.5"/></svg>
      www.VeloriaClinics.com
    </li>
    <li>
      <svg viewBox="0 0 20 20" aria-hidden="true"><rect x="2" y="4" width="16" height="12" rx="1" fill="none" stroke="#fff" stroke-width="2"/><path d="M2 5l8 6 8-6" fill="none" stroke="#fff" stroke-width="2"/></svg>
      info@VeloriaClinics.com
    </li>
  </ul>

  <p class="service-note">We will see patients and issue prescriptions and user cards, and we will align those patients with a federal grower who will deliver the meds (cannabis oil) to their place.</p>

  <div class="footer-brand">
    <span class="name">Veloria</span>
    <span class="tagline">Pain Management</span>
  </div>
</main>
</body>
</html>
```